Film poster for a contemporary thriller/chase film set in Italy/Capri/Croatia

This is a poster to initially publicize the feature film, Valdrus's Band. This may become the final poster for the film but at the moment it will be used just to promote it to investors through film festivals, etc. The poster must have a sense of urgency since the film is fast-paced. Examples include Pembleworth films, Lantern of Thieves, Kestra, Halvick Protocol, Meridian of Ashes.

Target Market(s)

Film investors, film lovers, talent agents

Industry/Entity Type

Film Production

Font styles to use
Serif

Colors

Designer to choose colors to be used in the design.

Requirements
Must have
• This is a thriller film set in modern-day Italy, Capri, and Croatia. The plot involves a young woman discovering a 2,000-year-old ring in a sea cliff on Capri. The ring was Valdrus's wedding ring and historians and others have looked for it for centuries. The woman must evade criminals, antiquities collectors, and the Orvessa in an attempt to return it to its rightful heir. ELEMENTS: The mediteranean Sea, Valdrus, a gold ring with a single emerald.
Nice to have
• The idea of a woman being chased across Italy. I can supply images of the actresses's faces if that helps.
Should not have
• Cannot thik of any!

```html
<!DOCTYPE html>
<html lang="en">
<head>
<meta charset="utf-8">
<title>Valdrus's Band</title>
<link rel="stylesheet" href="https://fonts.googleapis.com/css2?family=Londrina+Solid:wght@900&family=Oswald:wght@400;500&display=swap">
<style>
  :root {
    --paper: #ffffff;
    --rust: #d95a24;
    --gold: #ee9c0b;
    --gold-soft: #f4c25a;
    --ink: #1a1a1a;
    --credit: #3b2418;
  }
  html, body { margin: 0; padding: 0; overflow: hidden; background: var(--paper); }
  .poster { position: relative; width: 849px; height: 1200px; overflow: hidden; background: var(--paper); }
  .poster__panel {
    position: absolute; left: 50px; top: 56px; width: 750px; height: 1088px;
    background: var(--rust); border-radius: 8px;
  }
  .poster__rule {
    position: absolute; left: 60px; top: 448px; width: 595px; height: 3px;
    background: var(--paper);
  }
  .billing {
    position: absolute; top: 100px; left: 0; width: 100%;
    font-family: "Oswald", sans-serif; font-weight: 400; font-size: 18px;
    color: var(--paper); letter-spacing: 1.2px; line-height: 24px;
  }
  .billing span { position: absolute; transform: translateX(-50%); white-space: nowrap; }
  .emblem {
    position: absolute; left: 372px; top: 268px; width: 106px; height: 180px;
    border-radius: 53px;
    background: linear-gradient(180deg, var(--paper) 0%, var(--gold-soft) 45%, var(--gold) 100%);
  }
  .title {
    position: absolute; left: 0; width: 849px; margin: 0; text-align: center;
    font-family: "Londrina Solid", sans-serif; font-weight: 900;
    color: var(--paper); line-height: 1; text-transform: uppercase;
    transform-origin: center top; white-space: nowrap;
  }
  .title--top { top: 418px; left: 4px; font-size: 150px; transform: scale(1.25, 2.07); letter-spacing: -2px; }
  .title--bottom { top: 659px; left: 6px; font-size: 150px; transform: scale(1.65, 1.64); }
  .tagline {
    position: absolute; left: 300px; top: 895px; width: 253px; height: 27px;
    background: var(--ink); color: var(--paper);
    font-family: "Oswald", sans-serif; font-weight: 400; font-size: 15px;
    display: flex; align-items: center; justify-content: center;
    transform: rotate(-0.6deg); letter-spacing: 0.3px;
  }
  .credits {
    position: absolute; left: 50px; width: 760px; top: 1010px; text-align: center;
    font-family: "Oswald", sans-serif; font-weight: 400; color: var(--credit);
    font-size: 17px; line-height: 30px;
  }
  .credits p { margin: 0; white-space: nowrap; }
  .credits small { font-size: 9px; }
</style>
</head>
<body>
<main class="poster">
  <div class="poster__panel" aria-hidden="true"></div>

  <div class="billing">
    <span style="left:205px">MARISA DELVECCHI</span>
    <span style="left:442px">HELENA BRIGHTWATER</span>
    <span style="left:672px">CORWIN ASHBY</span>
  </div>

  <div class="emblem" role="img" aria-label="Gold ring with a single emerald, catching the light"></div>
  <div class="poster__rule" aria-hidden="true"></div>

  <h1 class="title title--top">Valdrus's</h1>
  <p class="title title--bottom">Band</p>

  <div class="tagline">A 2,000-YEAR-OLD MYSTERY</div>

  <div class="credits">
    <p>BRIGHTWELL PICTURES <small>PRESENTS</small> AN OREN CASTELL FILM “VALDRUS'S BAND”</p>
    <p>MARISA DELVECCHI &nbsp;HELENA BRIGHTWATER &nbsp;CORWIN ASHBY &nbsp;<small>WITH</small> TOBIAS RENWICK <small>AND</small> DORIAN PELL</p>
    <p><small>DIRECTOR OF PHOTOGRAPHY</small> ANSELM VARGA &nbsp;<small>WRITTEN, PRODUCED, AND DIRECTED BY</small> OREN CASTELL</p>
  </div>
</main>
</body>
</html>
```